Brontalex - Showroom Quality Auto - Motorcycle Wipes

Hello Designers. this should be a fun project if you like cars - or anything motor related.
My client got a design he was VERY disappointed with. So DO NOT anything close to this...lol.

I am hoping you can get most of this onto one page. This is a HIGH END wipe. It's $50. It's for people who care. I want it to look high end. I want it to be very guy focused. Car guru, motorcycle guru focused. We are looking at sticking with the Red and Black format but am open to other complimentary colors....as long as it looks amazing.

You can use the copy on there for now

Here are the website link to work off of.
https://otter-maple-rq8z.pagebuildery.com/
Password: brontalex2021

I will need this coded as well and will add this option to the pixel hive project. If there is more to do after, I will rehire you to finish this off.

The display stand gives you an idea of the colors we are using. Please keep it in this vein. Again open to complimentary colors.

Finally, again this is high end - car show quality.

```html
<!DOCTYPE html>
<html lang="en">
<head>
<meta charset="utf-8">
<title>Brontalex – Showroom Quality Auto &amp; Motorcycle Wipes</title>
<link rel="stylesheet" href="https://fonts.googleapis.com/css2?family=Teko:wght@400;500;600&family=Barlow:wght@400;500;600;700&display=swap">
<style>
:root{
  --red:#bf1e2d;
  --black:#111111;
  --white:#ffffff;
  --off:#f7f7f7;
  --stage:#fbf1f1;
  --hero:#e6e6e6;
  --hero-right:#dcdcdc;
  --grey-text:#6f6f6f;
  --line:#e2e2e2;
  --heading:'Teko',sans-serif;
  --body:'Barlow',sans-serif;
}
*{box-sizing:border-box;margin:0;padding:0}
html,body{width:1200px;height:3735px;overflow:hidden;background:var(--stage)}
.page{position:absolute;left:190px;top:24px;width:820px;height:3687px;background:var(--white);overflow:hidden;font-family:var(--body);color:var(--black)}
.abs{position:absolute}
h1,h2,h3,h4{font-family:var(--heading);font-weight:500;line-height:1}
p{font-size:9.5px;line-height:1.75;color:var(--grey-text)}
.photo{position:absolute}

/* hero */
.hero{position:absolute;left:0;top:0;width:820px;height:477px;background:var(--hero)}
.hero-right{position:absolute;left:470px;top:0;width:350px;height:477px;background:var(--hero-right)}
.nav{position:absolute;left:110px;top:24px;width:600px;height:60px;background:var(--black);display:flex;align-items:center;padding:0 22px}
.brand{display:flex;align-items:center;gap:8px;font-family:var(--heading);font-weight:500;font-size:26px;color:var(--white);letter-spacing:.5px;line-height:1}
.brand-dot{width:10px;height:10px;border-radius:50%;background:var(--red)}
.nav-links{margin-left:auto;display:flex;gap:26px;font-size:9px;color:#ccc;padding-right:24px;border-right:1px solid #333;height:60px;align-items:center}
.nav-links .active{color:var(--red)}
.nav-social{display:flex;gap:8px;padding-left:18px}
.nav-social span{width:7px;height:7px;border-radius:50%;background:#ddd}
.eyebrow{left:110px;top:181px;font-size:9px;letter-spacing:4px;color:var(--red);text-transform:uppercase}
.hero-title{left:110px;top:222px;font-size:40px;font-weight:600;line-height:1.12;text-transform:uppercase}
.hero-arrow{left:110px;top:300px}
.hero-car{left:428px;top:160px;width:392px;height:210px;background:linear-gradient(135deg,#d9d9d9,#c9323b 45%,#8e1119)}

/* product intro */
.product-box{left:110px;top:427px;width:290px;height:280px;background:var(--white)}
.product-img{left:60px;top:30px;width:175px;height:220px;background:linear-gradient(135deg,#3a3a3a,#d8d8d8)}
.intro-title{left:466px;top:548px;font-size:30px}
.intro-text{left:466px;top:594px;width:292px}

/* features */
.features{left:0;top:747px;width:820px;height:368px;background:var(--off)}
.feat{position:absolute;left:110px;width:250px}
.feat h3{font-size:17px;margin-bottom:6px}
.feat-photo{left:392px;top:78px;width:164px;height:212px;background:linear-gradient(160deg,#b81c28,#2a2a2a)}
.feat-card{left:568px;top:86px;width:142px;height:194px;background:var(--white);border:1px solid #ececec}
.feat-card .photo{left:20px;top:30px;width:102px;height:134px;background:linear-gradient(135deg,#3a3a3a,#161616)}

/* grid */
.grid{left:0;top:1115px;width:820px;height:410px;display:grid;grid-template-columns:repeat(4,205px);grid-template-rows:repeat(2,205px)}
.tile{position:relative;padding:38px 20px 0}
.tile h3{font-size:20px;color:var(--white);margin-bottom:12px}
.tile p{color:#e6e6e6;font-size:9px;line-height:1.8}
.tile-black{background:var(--black)}
.tile-red{background:var(--red)}
.tile-leaves{background:linear-gradient(135deg,#a04a18,#4a1e0a)}
.tile-door{background:linear-gradient(160deg,#6a6a6a,#262626)}
.tile-engine{background:linear-gradient(135deg,#a81a24,#3a3a3a)}
.tile-wheel{background:linear-gradient(135deg,#4a4a4a,#111)}

/* vehicles 1 */
.section-title{font-size:30px}
.moto-box{left:418px;top:1670px;width:402px;height:291px;background:linear-gradient(135deg,#efefef,#c63a44 55%,#6d1016)}
.tag{position:absolute;height:41px;background:var(--red);color:var(--white);font-family:var(--body);font-weight:700;font-size:10px;letter-spacing:.5px;display:flex;align-items:center;justify-content:center;text-transform:uppercase}
.tag-dark{background:var(--black)}
.check{position:absolute;display:flex;align-items:center;gap:7px;font-size:9px;color:#555}
.check::before{content:"";width:11px;height:11px;border-radius:50%;border:1.3px solid var(--red)}

/* video */
.video-title{left:0;width:820px;top:2020px;text-align:center;font-size:30px}
.video-sub{left:0;width:820px;top:2070px;text-align:center;font-size:9px}
.video{left:110px;top:2108px;width:600px;height:336px;background:linear-gradient(90deg,#b5b5b5,#2a2a2a 55%,#555)}
.play{left:384px;top:2254px;width:60px;height:60px;border-radius:50%;background:var(--red)}

/* vehicles 2 */
.car-box{left:0;top:2593px;width:402px;height:291px;background:linear-gradient(135deg,#f0f0f0,#3a3a3a 60%,#151515)}

/* icon features */
.ifeat{position:absolute;top:2950px;display:flex;gap:12px;align-items:center}
.ifeat h4{font-size:14px}
.ifeat p{font-size:8px;color:#aaa;line-height:1.4}
.divider{left:110px;top:3057px;width:600px;height:1px;background:var(--line)}

/* contact */
.contact-title{left:110px;top:3180px;font-size:30px}
.contact-text{left:110px;top:3218px;font-size:9px}
.contact-item{position:absolute;left:110px;padding-left:14px;border-left:2px solid var(--red)}
.contact-item h4{font-size:13px}
.contact-item p{font-size:8px;line-height:1.5}
.footer{left:0;top:3445px;width:820px;height:242px;background:#eeeeee}
.form{left:420px;top:3156px;width:290px;height:330px;background:var(--white);padding:22px 24px}
.form h3{font-family:Georgia,serif;font-weight:400;font-size:13px;color:#333;margin-bottom:14px}
.field label{display:block;font-size:7.5px;color:#666;margin-bottom:6px}
.field .input{height:24px;background:#f3f3f3;margin-bottom:14px}
.field .area{height:56px;background:#f3f3f3;margin-bottom:12px}
.submit{height:32px;background:var(--black);color:var(--white);font-size:8.5px;font-weight:700;display:flex;align-items:center;justify-content:center;letter-spacing:.5px}
.footer-brand{left:110px;top:3498px;font-family:var(--heading);font-weight:500;font-size:26px;color:var(--red);display:flex;align-items:center;gap:8px}
.footer-social{left:682px;top:3510px;display:flex;gap:8px}
.footer-social span{width:7px;height:7px;border-radius:50%;background:var(--black)}
.copyright{left:0;width:820px;top:3582px;text-align:center;font-size:8px;color:#888}
</style>
</head>
<body>
<main class="page">

  <section class="hero">
    <div class="hero-right"></div>
    <nav class="nav">
      <div class="brand"><span class="brand-dot"></span>Brontalex</div>
      <div class="nav-links"><span class="active">Home</span><span>Contact</span></div>
      <div class="nav-social"><span></span><span></span></div>
    </nav>
    <div class="abs eyebrow">Welcome to Brontalex</div>
    <h1 class="abs hero-title">Need a wipe<br>for your vehicle?</h1>
    <svg class="abs hero-arrow" width="12" height="22" viewBox="0 0 12 22"><path d="M6 1v19M1 15l5 5 5-5" fill="none" stroke="#bf1e2d" stroke-width="1.5"/></svg>
    <div class="photo hero-car" role="img" aria-label="Photo: red electric sedan, side three-quarter view"></div>
  </section>

  <div class="abs product-box">
    <div class="photo product-img" role="img" aria-label="Photo: black wipe canister with microfibre cloth"></div>
  </div>
  <h2 class="abs intro-title">The Only Wipe YOU NEED!</h2>
  <p class="abs intro-text">The Brontalex One Wipe is the ultimate cleaning tool. Pop the cap, take out the wipe and use it on any surface that needs cleaning. Once finished, wipe the residue away with the microfibre cloth provided. Use a rapid circular motion when wiping, please do not rub. Sit back and enjoy all the results!</p>

  <section class="abs features">
    <div class="feat" style="top:68px"><h3>Clean your vehicle anywhere</h3><p>Works on Cars, Trucks, Motorcycles, Bikes, RVs and any glass or leather surface.</p></div>
    <div class="feat" style="top:162px"><h3>Freedom Becomes A Choice</h3><p>There is no water needed. It is the ultimate cleaning and protection for any vehicle.</p></div>
    <div class="feat" style="top:255px"><h3>Next Level Clean</h3><p>Brontalex One Wipes clean any surface with minimal effort and maximum results.</p></div>
    <div class="photo feat-photo" role="img" aria-label="Photo: hand holding wipe canister against red car body"></div>
    <div class="abs feat-card"><div class="photo" role="img" aria-label="Photo: wipe canister with folded cloth"></div></div>
  </section>

  <section class="abs grid">
    <div class="tile tile-leaves" role="img" aria-label="Photo: wipe canister resting among autumn leaves"></div>
    <div class="tile tile-black"><h3>The one wipe.</h3><p>All your cleaning products in one wipe. Cleans and protects the inside and outside of any vehicle and your gear. No water, no brush, no equipment needed. The result will always be a high end finish.</p></div>
    <div class="tile tile-door" role="img" aria-label="Photo: car door panel interior, before and after cleaning"></div>
    <div class="tile tile-red"><h3>Works wonders.</h3><p>Insect impacts, grease, sludge, road salt, dust, tar, tree resin, shoe marks, hydro-carbons and all road dirt. No rinsing, no water source needed. Cleans leather, painted surfaces, glass, chrome, plastics, you name it, we've tried it</p></div>
    <div class="tile tile-red"><h3>Use on any vehicle.</h3><p>Cars, trucks, RVs, motorcycles, snowmobiles, bicycles, aviation. Whatever vehicle you enjoy spending your time in or on, Brontalex will clean and protect the inside and outside so it always has that showroom finish.</p></div>
    <div class="tile tile-engine" role="img" aria-label="Photo: cloth polishing a red motorcycle engine"></div>
    <div class="tile tile-black"><h3>High end look for <u>$50</u></h3><p>Lorem ipsum dolor sit amet, conset sectetur adipiscing elit, sed do mod eiusmod tempor incididunt ut labore et dolore magna aliqua. Ut enim ad minim veniam dorem</p></div>
    <div class="tile tile-wheel" role="img" aria-label="Photo: spoked motorcycle wheel beside wipe canister"></div>
  </section>

  <h2 class="abs section-title" style="left:110px;top:1588px">Works on any vehicle</h2>
  <p class="abs" style="left:466px;top:1590px;width:300px;font-size:8.5px">Water, equipment, space not required. Use literally anywhere, minimum effort, and amazing results!</p>
  <span class="check" style="left:110px;top:1766px">Exhaust</span><span class="check" style="left:192px;top:1766px">Chrome</span><span class="check" style="left:267px;top:1766px">Wheels</span>
  <span class="check" style="left:110px;top:1798px">Plastic</span><span class="check" style="left:192px;top:1798px">Leather</span><span class="check" style="left:267px;top:1798px">Saddlery</span>
  <span class="check" style="left:110px;top:1830px">Fairing</span><span class="check" style="left:192px;top:1830px">Plexiglass</span><span class="check" style="left:267px;top:1830px">Helmets</span>
  <span class="check" style="left:110px;top:1861px">Visor</span><span class="check" style="left:192px;top:1861px">Jackets</span><span class="check" style="left:267px;top:1861px">Gloves</span>
  <span class="check" style="left:110px;top:1893px">Boots</span><span class="check" style="left:192px;top:1893px">White wall tires</span>
  <div class="photo moto-box" role="img" aria-label="Photo: red sport motorcycle, side view"></div>
  <div class="tag" style="left:615px;top:1920px;width:205px">Anti rain &amp; anti-salt</div>

  <h2 class="abs video-title">Brontalex is the only wipe you will ever need</h2>
  <p class="abs video-sub">See the video below how Brontalex works</p>
  <div class="photo video" role="img" aria-label="Video still: hand holding the wipe canister"></div>
  <svg class="abs play" viewBox="0 0 60 60" role="img" aria-label="Play video"><circle cx="30" cy="30" r="30" fill="#bf1e2d"/><path d="M25 20l15 10-15 10z" fill="#fff"/></svg>

  <h2 class="abs section-title" style="left:110px;top:2510px">Works on any vehicle</h2>
  <p class="abs" style="left:466px;top:2512px;width:300px;font-size:8.5px">Cleans and protects all surfaces: matte shiny or covering all of kind of the surfaces and much more</p>
  <div class="photo car-box" role="img" aria-label="Photo: black sports coupe with red trim"></div>
  <div class="tag tag-dark" style="left:0;top:2843px;width:205px">Inside and outside</div>
  <span class="check" style="left:466px;top:2688px">Plastic</span><span class="check" style="left:558px;top:2688px">Headlights</span><span class="check" style="left:643px;top:2688px">Chrome</span>
  <span class="check" style="left:466px;top:2720px">Side Mirrors</span><span class="check" style="left:558px;top:2720px">Floor Mats</span><span class="check" style="left:643px;top:2720px">Dashboard</span>
  <span class="check" style="left:466px;top:2752px">Body</span><span class="check" style="left:558px;top:2752px">Windshield</span><span class="check" style="left:643px;top:2752px">Leather</span>
  <span class="check" style="left:466px;top:2783px">Windows</span><span class="check" style="left:558px;top:2783px">Wheels</span><span class="check" style="left:643px;top:2783px">Grille</span>

  <div class="ifeat" style="left:110px"><svg width="50" height="44" viewBox="0 0 50 44"><rect x="4" y="14" width="36" height="20" rx="4" fill="none" stroke="#bf1e2d" stroke-width="1.5"/><circle cx="13" cy="36" r="4" fill="none" stroke="#bf1e2d" stroke-width="1.5"/><circle cx="31" cy="36" r="4" fill="none" stroke="#bf1e2d" stroke-width="1.5"/><path d="M44 4v8M40 8h8" stroke="#bf1e2d" stroke-width="1.5"/></svg><div><h4>Feature Goes Here</h4><p>Lorem Ipsum Dolor Amet</p></div></div>
  <div class="ifeat" style="left:326px"><svg width="50" height="44" viewBox="0 0 50 44"><path d="M8 30l6-14h22l6 14v8H8z" fill="none" stroke="#bf1e2d" stroke-width="1.5"/><circle cx="16" cy="32" r="3" fill="none" stroke="#bf1e2d" stroke-width="1.5"/><circle cx="34" cy="32" r="3" fill="none" stroke="#bf1e2d" stroke-width="1.5"/><path d="M6 4v8M2 8h8M44 2v6M41 5h6" stroke="#bf1e2d" stroke-width="1.5"/></svg><div><h4>Feature Goes Here</h4><p>Lorem Ipsum Dolor Amet</p></div></div>
  <div class="ifeat" style="left:544px"><svg width="50" height="44" viewBox="0 0 50 44"><rect x="12" y="12" width="26" height="26" rx="3" fill="none" stroke="#bf1e2d" stroke-width="1.5"/><path d="M18 25l5 5 9-10" fill="none" stroke="#bf1e2d" stroke-width="1.5"/><path d="M44 4v8M40 8h8" stroke="#bf1e2d" stroke-width="1.5"/></svg><div><h4>Feature Goes Here</h4><p>Lorem Ipsum Dolor Amet</p></div></div>
  <div class="abs divider"></div>

  <div class="abs footer"></div>
  <h2 class="abs contact-title">Contact Brontalex</h2>
  <p class="abs contact-text">Get in touch with us, and we will get back to you as soon as possible.</p>
  <div class="contact-item" style="top:3272px"><h4>Call us at-</h4><p>555 018 2244</p></div>
  <div class="contact-item" style="top:3336px"><h4>Mail us at-</h4><p>garage@brontalex.com</p></div>
  <form class="abs form">
    <h3>Contact Form</h3>
    <div class="field"><label>Full Name*</label><div class="input"></div></div>
    <div class="field"><label>Email Address*</label><div class="input"></div></div>
    <div class="field"><label>Phone Number*</label><div class="input"></div></div>
    <div class="field"><label>Message*</label><div class="area"></div></div>
    <div class="submit">SUBMIT YOUR MESSAGE</div>
  </form>
  <div class="abs footer-brand"><span class="brand-dot"></span>Brontalex</div>
  <div class="abs footer-social"><span></span><span></span></div>
  <p class="abs copyright">Copyright 2021 - Brontalex - All rights reserved</p>

</main>
</body>
</html>
```